Business Card for my New Brokerage

Looking to get a business card design for my new Real Estate Brokerage.
I want it with Picture, Phone Number, Email, Website, Office Address
Name and Designation. Please add logo too.

Target Market(s)

Real Estate Investors or Home Buyers

Industry/Entity Type

Real Estate

Contact Information for Business Card

Name, Email, Phone Number, website, email, office address

Colors
EB3D1F
EC4F4E
F09395
F8D3D4
FCEDEE

Requirements
Must have
• Minimalistic, Clean, Modern, Photo
Nice to have
• White and Red Colors

```html
<!DOCTYPE html>
<html lang="en">
<head>
<meta charset="utf-8">
<title>Ember Realty Co — Business Card</title>
<link rel="stylesheet" href="https://fonts.googleapis.com/css2?family=Montserrat:wght@700&family=Poppins:wght@400;600&display=swap">
<style>
  :root {
    --red: #e01f26;
    --red-deep: #c8141c;
    --red-soft: #e83a3f;
    --white: #ffffff;
    --ink: #1c1c1c;
    --stage: #e9e9ea;
    --photo-navy: #23395b;
    --photo-light: #dfe6ee;
  }
  * { box-sizing: border-box; margin: 0; padding: 0; }
  html, body {
    width: 1200px; height: 900px; overflow: hidden;
    background: var(--stage);
  }
  .canvas { position: relative; width: 1200px; height: 900px; }

  .card {
    position: absolute;
    width: 700px; height: 400px;
    border-radius: 24px;
    box-shadow: 0 10px 30px rgba(0,0,0,.18);
    overflow: hidden;
  }

  /* Front */
  .card-front {
    left: 440px; top: 40px;
    background: linear-gradient(135deg, var(--red-soft) 0%, var(--red) 55%, var(--red-deep) 100%);
    display: flex; align-items: center; justify-content: center;
  }
  .brand {
    display: flex; align-items: center; gap: 14px;
    font-family: "Montserrat", sans-serif; font-weight: 700;
    letter-spacing: .04em; text-transform: uppercase;
  }
  .brand-mark { width: 14px; height: 14px; }
  .card-front .brand { color: var(--white); font-size: 52px; }
  .card-front .brand-mark { width: 20px; height: 20px; background: var(--white); }

  /* Back */
  .card-back {
    left: 60px; top: 460px;
    background: var(--white);
    font-family: "Poppins", sans-serif;
    color: var(--ink);
  }
  .card-back .brand {
    position: absolute; left: 56px; top: 48px;
    color: var(--red); font-size: 34px;
  }
  .card-back .brand-mark { background: var(--red); }

  .person { position: absolute; left: 56px; top: 122px; }
  .person-name {
    font-weight: 600; font-size: 26px; color: var(--red);
    text-transform: uppercase; line-height: 1.1;
  }
  .person-role { font-size: 16px; margin-top: 2px; }

  .divider {
    position: absolute; left: 48px; top: 200px;
    width: 396px; height: 2px; background: var(--red);
  }

  .contact-list {
    position: absolute; left: 56px; top: 220px;
    list-style: none; font-size: 17px; line-height: 1.75;
  }
  .contact-list li { display: flex; align-items: center; gap: 10px; }
  .contact-list svg { width: 16px; height: 16px; flex: none; }

  .portrait-frame {
    position: absolute; left: 444px; top: 60px;
    width: 206px; height: 270px;
    border: 2px solid var(--red);
    padding: 0;
  }
  .portrait {
    width: 100%; height: 100%;
    background: linear-gradient(180deg, var(--white) 0%, var(--photo-light) 45%, var(--photo-navy) 100%);
  }

  .office-address {
    position: absolute; right: 48px; top: 340px;
    text-align: right; font-size: 15px; line-height: 1.35;
    font-style: normal;
  }
</style>
</head>
<body>
<main class="canvas">

  <section class="card card-front" aria-label="Card front">
    <div class="brand">
      <span class="brand-name">Ember Realty Co</span>
      <span class="brand-mark" aria-hidden="true"></span>
    </div>
  </section>

  <section class="card card-back" aria-label="Card back">
    <div class="brand">
      <span class="brand-name">Ember Realty Co</span>
      <span class="brand-mark" aria-hidden="true"></span>
    </div>

    <div class="person">
      <h1 class="person-name">Daniel Reyes</h1>
      <p class="person-role">Owner/CEO</p>
    </div>

    <div class="divider" aria-hidden="true"></div>

    <ul class="contact-list">
      <li>
        <svg viewBox="0 0 24 24" aria-hidden="true"><path fill="#e01f26" d="M6.6 10.8a15 15 0 0 0 6.6 6.6l2.2-2.2a1 1 0 0 1 1-.25 11.4 11.4 0 0 0 3.6.57 1 1 0 0 1 1 1V20a1 1 0 0 1-1 1A17 17 0 0 1 3 4a1 1 0 0 1 1-1h3.5a1 1 0 0 1 1 1c0 1.25.2 2.45.57 3.57a1 1 0 0 1-.25 1z"/></svg>
        123-555-01890
      </li>
      <li>
        <svg viewBox="0 0 24 24" aria-hidden="true"><rect x="2" y="5" width="20" height="14" rx="1" fill="#e01f26"/><path d="M3 6l9 7 9-7" fill="none" stroke="#fff" stroke-width="1.6"/></svg>
        hello@emberrealtyco.com
      </li>
      <li>
        <svg viewBox="0 0 24 24" aria-hidden="true"><circle cx="12" cy="12" r="10" fill="#e01f26"/><path d="M2 12h20M12 2c3 3 3 17 0 20M12 2c-3 3-3 17 0 20" fill="none" stroke="#fff" stroke-width="1.4"/></svg>
        www.emberrealtyco.com
      </li>
    </ul>

    <div class="portrait-frame">
      <div class="portrait" role="img" aria-label="Headshot of the broker in a navy blazer and light blue shirt"></div>
    </div>

    <address class="office-address">
      1450 Harbor View Road<br>
      Maple County Name 4120
    </address>
  </section>

</main>
</body>
</html>
```